BrivoMatex. Lantern for the Steady Growth. Business card

Professional business card for BrivoMatex (Lantern for the Steady Growth)
My rationale: Strategy-> Execution-> Results-> Value that lead to the BrivoMatex name: We put the Lantern for the Steady Growth.
We deliver value to our customers helping them at defining a good strategy (cyan arrow). 90% of well formulated strategies fail due to poor execution so we also consider strategical execution very important (green arrow). Due to the execution we obtain the results (blue arrow). Finally, the results provide feedback to redefine strategy, and the new strategy has to be executed and new results obtained providing new feedback and on and on. It's like a wheel that finally, must create corporate value: value for shareholders, staholders, employees, providers...-

Target Market(s)

CEOs and steering comitees , invewrnent funds

Industry/Entity Type

Business Consultant

Contact Information for Business Card

Tommaso Ferlini
CEO & Founder
tommaso.ferlini@brivomatex.example
Mobile: +34 611.205.938
www.brivomatex.example

Colors

Designer to choose colors to be used in the design.

Requirements
Nice to have
• Nice to hace the words: Strategy, execution, results
• Nice to vave the claim: Lantern for the Steady Growth
• The three colors should be shown:
• cyan for STRATEGY
• green for EXECUTION
• blue for RESULTS
Should not have
• Complete black background

```html
<!DOCTYPE html>
<html lang="en">
<head>
<meta charset="utf-8">
<title>BrivoMatex – Business Card</title>
<link href="https://fonts.googleapis.com/css2?family=Arimo:wght@400;700&display=swap" rel="stylesheet">
<style>
  :root {
    --page-bg: #e4e2de;
    --brand-blue: #0d2f93;
    --strategy-cyan: #1aa3e0;
    --execution-green: #8cc63f;
    --card-white: #f4f4f4;
    --logo-panel: #eaeaea;
    --ink: #111111;
    --ink-soft: #2a2a2a;
  }
  html, body {
    margin: 0;
    padding: 0;
    width: 1200px;
    height: 1200px;
    overflow: hidden;
    background: var(--page-bg);
    font-family: "Arimo", Arial, sans-serif;
  }
  .business-card {
    position: absolute;
    left: 100px;
    top: 290px;
    width: 1000px;
    height: 620px;
    background: var(--card-white);
    box-shadow: 0 10px 30px rgba(0,0,0,0.18);
    overflow: hidden;
  }
  .edge-band {
    position: absolute;
    left: 0;
    top: 0;
    width: 110px;
    height: 620px;
    background: var(--brand-blue);
  }
  .growth-artwork {
    position: absolute;
    right: 0;
    bottom: 0;
    width: 250px;
    height: 300px;
    background: linear-gradient(160deg, var(--brand-blue) 0%, var(--brand-blue) 40%, var(--execution-green) 72%, var(--strategy-cyan) 100%);
  }
  .brand-panel {
    position: absolute;
    left: 190px;
    top: 70px;
    width: 290px;
    height: 200px;
    background: var(--logo-panel);
    display: flex;
    align-items: center;
    justify-content: center;
    gap: 12px;
  }
  .brand-mark {
    width: 22px;
    height: 22px;
    background: var(--brand-blue);
  }
  .brand-name {
    color: var(--brand-blue);
    font-weight: 700;
    font-size: 40px;
    letter-spacing: -0.5px;
  }
  .person {
    position: absolute;
    left: 560px;
    top: 62px;
  }
  .person-name {
    margin: 0;
    font-size: 32px;
    font-weight: 700;
    color: var(--ink);
  }
  .person-role {
    margin: 6px 0 0;
    font-size: 27px;
    font-weight: 400;
    color: var(--ink-soft);
  }
  .contact-list {
    position: absolute;
    left: 200px;
    top: 300px;
    margin: 0;
    padding: 0;
    list-style: none;
  }
  .contact-item {
    display: flex;
    align-items: center;
    gap: 16px;
    font-size: 27px;
    color: var(--ink);
    height: 52px;
  }
  .contact-icon {
    width: 30px;
    height: 30px;
    flex: none;
  }
</style>
</head>
<body>
  <div class="business-card">
    <div class="edge-band"></div>
    <div class="growth-artwork" role="img" aria-label="Rising arrow artwork in blue, green and cyan"></div>

    <div class="brand-panel">
      <span class="brand-mark"></span>
      <span class="brand-name">BrivoMatex</span>
    </div>

    <div class="person">
      <h1 class="person-name">Tommaso Ferlini</h1>
      <p class="person-role">CEO &amp; Founder</p>
    </div>

    <ul class="contact-list">
      <li class="contact-item">
        <svg class="contact-icon" viewBox="0 0 30 30" aria-hidden="true">
          <rect x="3" y="7" width="24" height="16" fill="none" stroke="var(--strategy-cyan)" stroke-width="2.5"/>
          <path d="M3 7 L15 17 L27 7" fill="none" stroke="var(--strategy-cyan)" stroke-width="2.5"/>
        </svg>
        tommaso.ferlini@brivomatex.example
      </li>
      <li class="contact-item">
        <svg class="contact-icon" viewBox="0 0 30 30" aria-hidden="true">
          <rect x="9" y="3" width="13" height="24" rx="3" fill="var(--strategy-cyan)"/>
          <rect x="11.5" y="6.5" width="8" height="8" fill="#ffffff"/>
        </svg>
        +34 611.205.938
      </li>
      <li class="contact-item">
        <svg class="contact-icon" viewBox="0 0 30 30" aria-hidden="true">
          <circle cx="14" cy="14" r="11" fill="none" stroke="var(--strategy-cyan)" stroke-width="2.5"/>
          <ellipse cx="14" cy="14" rx="5" ry="11" fill="none" stroke="var(--strategy-cyan)" stroke-width="2"/>
          <path d="M3 14 H25" stroke="var(--strategy-cyan)" stroke-width="2"/>
        </svg>
        www.brivomatex.example
      </li>
    </ul>
  </div>
</body>
</html>
```